Opal Meadow Signage

Please I'm looking to have signage for business front door and 2 windows. Wow me! It is the first thing ppl will see always.
I'm looking to have some privacy because I am in the beauty business, so privacy is key. Please look at attached pictures of front and windows. Make it elegant because the spa shop is all about luxury excellence. I need website, Email address phone number in name of the company. I'd like to also put some services somewhere on the signage (s) you can place it where you'd think it would be best. Lymphatic Drainage, Body Sculpting/contouring, Detoxing, Cavitation, Facials ..... and much more

```html
<!DOCTYPE html>
<html lang="en">
<head>
<meta charset="utf-8">
<title>Opal Meadow Signage</title>
<link href="https://fonts.googleapis.com/css2?family=Marcellus&family=Marcellus+SC&family=Cormorant+Garamond:wght@500&display=swap" rel="stylesheet">
<style>
  :root {
    --bg: #2b2b2b;
    --violet: #5b1cf0;
    --violet-deep: #4a12d6;
    --ink: #1d1560;
    --white: #ffffff;
  }
  html, body {
    margin: 0;
    padding: 0;
    width: 1200px;
    height: 1200px;
    overflow: hidden;
    background: var(--bg);
  }
  .canvas {
    position: relative;
    width: 1200px;
    height: 1200px;
  }
  .window-panel {
    position: absolute;
    background: var(--violet);
    color: var(--white);
    font-family: "Marcellus", serif;
    display: flex;
    align-items: center;
    justify-content: center;
    overflow: hidden;
  }
  .window-panel--tall {
    left: 70px; top: 250px; width: 220px; height: 720px;
  }
  .window-panel--tall .window-word {
    transform: rotate(90deg);
    font-size: 128px;
    letter-spacing: 4px;
    white-space: nowrap;
  }
  .window-panel--wide {
    left: 310px; top: 280px; width: 400px; height: 230px;
  }
  .window-panel--wide .window-word {
    font-size: 118px;
    letter-spacing: 3px;
  }
  .door-panel {
    position: absolute;
    left: 770px; top: 200px; width: 340px; height: 800px;
    background: var(--white);
  }
  .services-banner {
    position: absolute;
    left: 20px; top: 0; width: 300px; height: 470px;
  }
  .services-list {
    position: absolute;
    left: 20px; top: 32px; width: 300px;
    margin: 0; padding: 0;
    list-style: none;
    text-align: center;
    font-family: "Marcellus SC", serif;
    color: var(--white);
    font-size: 29px;
    line-height: 1.02;
  }
  .services-list li { padding: 0 10px; }
  .services-list .divider {
    width: 110px; height: 1px;
    margin: 14px auto;
    background: var(--white);
    opacity: 0.85;
  }
  .brand {
    position: absolute;
    left: 0; top: 520px; width: 340px;
    text-align: center;
  }
  .brand-dot {
    width: 96px; height: 96px;
    margin: 0 auto 16px;
    border-radius: 50%;
    background: var(--violet);
  }
  .brand-name {
    font-family: "Marcellus", serif;
    color: var(--violet);
    font-size: 40px;
    line-height: 1;
    letter-spacing: 1px;
  }
  .brand-tagline {
    font-family: "Marcellus", serif;
    color: var(--violet-deep);
    font-size: 10.5px;
    letter-spacing: 0.6px;
    margin-top: 6px;
    text-transform: uppercase;
  }
  .contact {
    position: absolute;
    left: 0; top: 718px; width: 340px;
    text-align: center;
    color: var(--ink);
    font-family: "Cormorant Garamond", serif;
  }
  .contact-phone {
    font-size: 40px;
    line-height: 1;
    display: flex;
    align-items: center;
    justify-content: center;
    gap: 4px;
  }
  .contact-web {
    font-size: 19px;
    margin-top: 4px;
    letter-spacing: 0.5px;
  }
  .contact-web .accent { color: var(--violet); }
</style>
</head>
<body>
<main class="canvas">
  <section class="window-panel window-panel--tall">
    <span class="window-word">MEADOW</span>
  </section>
  <section class="window-panel window-panel--wide">
    <span class="window-word">OPAL</span>
  </section>

  <section class="door-panel">
    <svg class="services-banner" viewBox="0 0 300 470" aria-hidden="true">
      <path d="M0 0 H300 V430 Q300 440 290 440 H180 L150 470 L120 440 H10 Q0 440 0 430 Z" fill="var(--violet)"/>
    </svg>
    <ul class="services-list">
      <li>Lymphatic<br>Drainage</li>
      <li class="divider" aria-hidden="true"></li>
      <li>Body Sculpting/<br>Contouring</li>
      <li class="divider" aria-hidden="true"></li>
      <li>Detoxing</li>
      <li class="divider" aria-hidden="true"></li>
      <li>Cavitation</li>
      <li class="divider" aria-hidden="true"></li>
      <li>Facials</li>
    </ul>

    <div class="brand">
      <div class="brand-dot" aria-hidden="true"></div>
      <div class="brand-name">OPAL MEADOW</div>
      <div class="brand-tagline">Where beauty and wellness find harmony</div>
    </div>

    <div class="contact">
      <div class="contact-phone">
        <svg width="22" height="26" viewBox="0 0 24 24" aria-hidden="true">
          <path d="M6.6 10.8c1.4 2.8 3.8 5.1 6.6 6.6l2.2-2.2c.3-.3.7-.4 1-.2 1.1.4 2.3.6 3.6.6.6 0 1 .4 1 1V20c0 .6-.4 1-1 1C10.6 21 3 13.4 3 4c0-.6.4-1 1-1h3.5c.6 0 1 .4 1 1 0 1.3.2 2.5.6 3.6.1.3 0 .7-.2 1L6.6 10.8z" fill="var(--ink)"/>
        </svg>
        <span>555.284.0192</span>
      </div>
      <div class="contact-web">WWW.<span class="accent">OPALMEADOW</span>.COM</div>
    </div>
  </section>
</main>
</body>
</html>
```